Stationery set created from logo

Existing logo design from successful designer T94. Thanks T94.

We now now need letterhead, business card design and background slide for powerpoint presentations. These need to be provided as PDF; JPEG and AI files.

I also need the names of the fonts used and the RGB colour/PMS colour names

Thankyou for submitting your designs. A design has been selcted. I appreciate youtr work. God wishes to you

```html
<!DOCTYPE html>
<html lang="en">
<head>
<meta charset="utf-8">
<title>CLMA Presentation Background</title>
<link rel="stylesheet" href="https://fonts.googleapis.com/css2?family=Arimo:wght@400;700&display=swap">
<style>
  :root {
    --page: #ffffff;
    --frame-line: #9a9a9a;
    --swoosh: #efeef3;
    --navy: #2a2556;
    --band-text: #ffffff;
  }
  html, body {
    margin: 0;
    padding: 0;
    width: 1200px;
    height: 900px;
    overflow: hidden;
    background: var(--page);
  }
  .slide {
    position: relative;
    width: 1200px;
    height: 900px;
    background: var(--page);
  }
  .slide-frame {
    position: absolute;
    left: 40px;
    top: 37px;
    width: 1119px;
    height: 840px;
    box-sizing: border-box;
    border: 1px solid var(--frame-line);
    overflow: hidden;
    background: var(--page);
  }
  .swooshes {
    position: absolute;
    inset: 0;
  }
  .brand {
    position: absolute;
    left: 0;
    right: 0;
    top: 56px;
    display: flex;
    flex-direction: column;
    align-items: center;
    gap: 10px;
  }
  .brand-dot {
    width: 30px;
    height: 30px;
    border-radius: 50%;
    background: var(--navy);
  }
  .brand-name {
    font-family: "Arimo", Arial, sans-serif;
    font-weight: 700;
    font-size: 44px;
    letter-spacing: 2px;
    line-height: 1;
    color: var(--navy);
    margin: 0;
  }
  .footer-band {
    position: absolute;
    left: 0;
    right: 0;
    top: 800px;
    height: 26px;
    background: var(--navy);
    display: flex;
    align-items: center;
    justify-content: center;
  }
  .footer-url {
    font-family: "Arimo", Arial, sans-serif;
    font-weight: 400;
    font-size: 15px;
    letter-spacing: 0.5px;
    color: var(--band-text);
  }
</style>
</head>
<body>
  <div class="slide">
    <div class="slide-frame">
      <svg class="swooshes" width="1119" height="840" viewBox="0 0 1119 840" aria-hidden="true">
        <rect class="swoosh-field" width="1119" height="840" fill="var(--swoosh)"/>
        <ellipse class="content-oval" cx="560" cy="380" rx="548" ry="369" fill="var(--page)"/>
        <!-- top-left corner and gap -->
        <path fill="var(--page)" d="M0,0 L62,0 C38,32 16,70 0,108 Z"/>
        <path fill="var(--page)"
          d="M115,0 L350,0 C250,60 150,150 78,235 L70,300 C72,180 88,80 115,0 Z"/>
        <!-- bottom-right corner and gap -->
        <path fill="var(--page)" d="M1119,650 C1080,720 1010,790 945,840 L1119,840 Z"/>
        <path fill="var(--page)"
          d="M1075,498 C990,610 860,750 700,840 L880,840 C920,780 945,700 960,640 Z"/>
      </svg>

      <header class="brand">
        <span class="brand-dot"></span>
        <h1 class="brand-name">CLMA</h1>
      </header>

      <footer class="footer-band">
        <span class="footer-url">WWW.CLMA.ORG.AU</span>
      </footer>
    </div>
  </div>
</body>
</html>
```